Custom Cakes- Nonprofit Organization Stationery Set

We are looking for a FULL set stationery design for our organization.
We create custom cakes for children in foster care and work with teens and young adults who have intellectual and developmental disabilities.
We spare no expense or amount of time creating fantastic cakes for these kids.... therefore are marketing materials need to reflect the same amount of fine details.

* Business Card Design (Front/Back preferred)
* Letterhead
* Envelope
* Presentation Folder

**** Tagline: Baking Joyful Moments
would like this to appear on business card and marketing materials

Delia Marsh - Founder/Executive Director
www.marburycakes.org
info@marburycakes.org
1-844-TO-MARBRY
1-844-555-0172

Address is optional
PO Box 7316
Alpharetta, GA 30091

• Contact Information
• PO Box Address, design that will go well with textured/colored business card paper
• Updated: Business cards (maybe) textured paper, foiled, embossed or colored edges

```html
<!DOCTYPE html>
<html lang="en">
<head>
<meta charset="utf-8">
<title>Marbury Celebration Trust – Presentation Folder, Inside Spread</title>
<link rel="stylesheet" href="https://fonts.googleapis.com/css2?family=Open+Sans:wght@400;600&display=swap">
<style>
  :root {
    --backdrop: #e6e6e6;
    --paper: #ffffff;
    --fold-shade: #efefef;
    --magenta: #e91e8f;
    --pocket: #111111;
    --ink: #222222;
    --tagline: #6b6b6b;
    --cake-pink: #f7dcea;
    --cake-yellow: #fbf3c8;
    --cake-green: #e8f2dc;
    --cake-blue: #e4f1f7;
    --cake-stand: #dcdcdc;
  }
  * { box-sizing: border-box; margin: 0; padding: 0; }
  html, body {
    width: 1200px;
    height: 1000px;
    overflow: hidden;
    background: var(--backdrop);
    font-family: "Open Sans", Arial, sans-serif;
  }
  .canvas {
    position: relative;
    width: 1200px;
    height: 1000px;
  }
  .folder-spread {
    position: absolute;
    left: 180px;
    top: 200px;
    width: 840px;
    height: 600px;
    display: flex;
    box-shadow: 0 18px 40px rgba(0,0,0,0.18);
  }
  .panel {
    position: relative;
    width: 420px;
    height: 600px;
    background: var(--paper);
    overflow: hidden;
  }
  .panel--left {
    background: linear-gradient(to right, var(--paper) 85%, var(--fold-shade));
  }
  .panel--right {
    background: linear-gradient(to left, var(--paper) 85%, var(--fold-shade));
  }
  .cake-art {
    position: absolute;
    left: 90px;
    top: 210px;
    width: 240px;
    height: 250px;
    border-radius: 12px;
    background: linear-gradient(180deg,
      var(--cake-yellow) 0%,
      var(--cake-pink) 30%,
      var(--cake-green) 55%,
      var(--cake-blue) 75%,
      var(--cake-stand) 100%);
    opacity: 0.75;
  }
  .side-flap {
    position: absolute;
    right: 0;
    top: 0;
    width: 52px;
    height: 600px;
    background: var(--magenta);
  }
  .pocket {
    position: absolute;
    left: 0;
    bottom: 0;
    width: 420px;
    height: 210px;
  }
  .pocket svg { display: block; }
  .card-slot {
    position: absolute;
    left: 50px;
    top: 62px;
    width: 230px;
    height: 128px;
  }
  .card-slot svg { position: absolute; inset: 0; }
  .card-content {
    position: absolute;
    inset: 0;
    display: flex;
    flex-direction: column;
    align-items: center;
    justify-content: center;
    gap: 8px;
  }
  .brand {
    display: flex;
    align-items: center;
    gap: 6px;
  }
  .brand-square {
    width: 12px;
    height: 12px;
    background: var(--magenta);
  }
  .brand-name {
    font-size: 13px;
    font-weight: 600;
    color: var(--ink);
    white-space: nowrap;
  }
  .tagline {
    font-size: 11px;
    font-weight: 400;
    color: var(--tagline);
    letter-spacing: 0.2px;
    white-space: nowrap;
  }
</style>
</head>
<body>
<main class="canvas">
  <section class="folder-spread">
    <div class="panel panel--left">
      <div class="cake-art" role="img" aria-label="Faint illustration of stacked gift-box cake tiers with ribbons on a cake stand"></div>
    </div>
    <div class="panel panel--right">
      <div class="side-flap"></div>
      <div class="pocket">
        <svg width="420" height="210" viewBox="0 0 420 210" aria-hidden="true">
          <polygon points="0,40 280,0 420,40 420,210 0,210" fill="var(--pocket)"/>
        </svg>
        <div class="card-slot">
          <svg width="230" height="128" viewBox="0 0 230 128" aria-hidden="true">
            <rect x="0" y="0" width="230" height="128" fill="var(--paper)"/>
            <polygon points="0,0 40,0 0,40" fill="var(--pocket)"/>
            <polygon points="230,128 190,128 230,88" fill="var(--pocket)"/>
          </svg>
          <div class="card-content">
            <div class="brand">
              <span class="brand-square"></span>
              <span class="brand-name">Marbury Celebration Trust</span>
            </div>
            <p class="tagline">Baking Joyful Moments</p>
          </div>
        </div>
      </div>
    </div>
  </section>
</main>
</body>
</html>
```